Email Banner for Technology Company

We need a new email banner. The purpose of the email banner is to make us look more professional as a business and keep all communications with clients uniform. The previous designs which we have included below have now become outdated as our brand has developed and we need the new banner to become more aligned and modern.
We are a marketing organization that specialises in lead generation, email newsletters are sent to prospects on a regular basis. Therefore, it is important that we have an aesthetically pleasing banner as this is the first real impression prospects have our business. First impressions matter.
We are looking for a new email banner design as the current design is now outdated and does not reflect who we are as a business.
The new banners are required for launch at the start of Q2.
There is future work in the pipeline for the winning design. We have multiple industry sites that will require the new design as well as creating each of these in multiple languages.
The design must include the Brightwave Briefings wording the tagline 'Where Tech Leaders Find Insight'.
It needs to be creative and fun but still remain professional, sticking with the colour theme that already exists.

```html
<!DOCTYPE html>
<html lang="en">
<head>
<meta charset="utf-8">
<title>Brightwave Briefings – Email Banner</title>
<link rel="stylesheet" href="https://fonts.googleapis.com/css2?family=Barlow:wght@700&family=Barlow+Condensed:wght@400&display=swap">
<style>
  :root {
    --blue-bright: #1a95dc;
    --blue-mid: #0a6fb4;
    --blue-deep: #083d6e;
    --blue-glow: #7fcaf0;
    --name-blue: #0a9be0;
    --panel-white: #ffffff;
    --tagline-band: #837dbb;
    --text-white: #ffffff;
  }
  html, body {
    margin: 0;
    padding: 0;
    overflow: hidden;
    background: #ffffff;
  }
  .banner {
    position: relative;
    width: 1200px;
    height: 306px;
    overflow: hidden;
  }
  .banner__backdrop,
  .banner__shapes {
    position: absolute;
    inset: 0;
    width: 1200px;
    height: 306px;
    display: block;
  }
  .banner__name {
    position: absolute;
    left: 138px;
    top: 78px;
    margin: 0;
    font-family: "Barlow", "Arial", sans-serif;
    font-weight: 700;
    font-size: 100px;
    line-height: 1;
    letter-spacing: -1.5px;
    color: var(--text-white);
    white-space: nowrap;
  }
  .banner__name-lead {
    color: var(--name-blue);
    margin-right: 10px;
  }
  .banner__tagline {
    position: absolute;
    left: 349px;
    top: 199px;
    margin: 0;
    font-family: "Barlow Condensed", "Arial Narrow", sans-serif;
    font-weight: 400;
    font-size: 46px;
    line-height: 57px;
    color: var(--text-white);
    white-space: nowrap;
  }
</style>
</head>
<body>
  <div class="banner">
    <svg class="banner__backdrop" role="img" aria-label="Photograph of glowing blue fibre-optic strands fanning out into the distance" viewBox="0 0 1200 306">
      <defs>
        <linearGradient id="backdrop-horizontal" x1="0" y1="0" x2="1" y2="0">
          <stop offset="0" stop-color="var(--blue-bright)"/>
          <stop offset="0.45" stop-color="var(--blue-mid)"/>
          <stop offset="1" stop-color="var(--blue-deep)"/>
        </linearGradient>
        <linearGradient id="backdrop-floor" x1="0" y1="0" x2="0" y2="1">
          <stop offset="0.55" stop-color="var(--blue-glow)" stop-opacity="0"/>
          <stop offset="1" stop-color="var(--blue-glow)" stop-opacity="0.75"/>
        </linearGradient>
      </defs>
      <rect width="1200" height="306" fill="url(#backdrop-horizontal)"/>
      <rect width="1200" height="306" fill="url(#backdrop-floor)"/>
    </svg>

    <svg class="banner__shapes" viewBox="0 0 1200 306" aria-hidden="true">
      <defs>
        <linearGradient id="name-panel-fade" x1="0" y1="0" x2="0" y2="1">
          <stop offset="0" stop-color="var(--panel-white)" stop-opacity="1"/>
          <stop offset="0.45" stop-color="var(--panel-white)" stop-opacity="0.7"/>
          <stop offset="1" stop-color="var(--panel-white)" stop-opacity="0.1"/>
        </linearGradient>
      </defs>
      <polygon class="name-panel" points="85,71 642,71 776,306 218,306" fill="url(#name-panel-fade)"/>
      <polygon class="tagline-band" points="291,199 1020,199 1052,256 322,256" fill="var(--tagline-band)"/>
    </svg>

    <h1 class="banner__name"><span class="banner__name-lead">Brightwave</span>Briefings</h1>
    <p class="banner__tagline">Where Tech Leaders Find Insight</p>
  </div>
</body>
</html>
```